Tallgrove Vale Management

I need a professional website. My current website is tallgrovevalemanagement.com and I hate it. It was created with some AI tool very quickly because I needed a site up and running with no advanced notice. I’m open to all designs .. I trust you, the professionals will deliver the results I’m anxiously awaiting! :)

```html
<!DOCTYPE html>
<html lang="en">
<head>
<meta charset="utf-8">
<title>Tallgrove Vale Management</title>
<link href="https://fonts.googleapis.com/css2?family=Outfit:wght@300;400;500;600;700;800&display=swap" rel="stylesheet">
<style>
:root{
  --navy:#1c2a4e;
  --navy-deep:#16223f;
  --red:#cf2a2e;
  --mist:#f2f3f5;
  --ink:#2b3550;
  --white:#ffffff;
}
*{box-sizing:border-box;margin:0;padding:0}
html,body{width:1200px;height:2991px;overflow:hidden;background:var(--white)}
body{font-family:'Outfit',sans-serif;color:var(--ink)}
.page{position:relative;width:1200px;height:2991px;overflow:hidden}
.abs{position:absolute}
svg.layer{position:absolute;left:0;top:0}

/* brand wordmark */
.brand{position:absolute;display:flex;align-items:center;gap:8px;color:var(--white);font-weight:700;text-transform:uppercase;line-height:1.05;letter-spacing:.5px}
.brand-square{width:12px;height:12px;background:var(--red);flex:none}

/* nav */
.nav{position:absolute;top:39px;right:150px;display:flex;gap:30px;font-size:10px;font-weight:500;letter-spacing:.3px}
.nav a{color:var(--white);text-decoration:none;position:relative}
.nav a.is-active{color:var(--red)}
.nav a.is-active::after{content:"";position:absolute;left:0;right:0;bottom:-7px;height:2px;background:var(--red)}

/* hero */
.hero-kicker{left:0;width:1200px;top:297px;text-align:center;color:var(--white);font-size:18px;font-weight:400;letter-spacing:.2px}
.hero-title{left:0;width:1200px;top:322px;text-align:center;color:var(--white);font-size:58px;font-weight:800;line-height:52px;letter-spacing:-1px;text-transform:uppercase}
.btn{position:absolute;display:flex;align-items:center;justify-content:center;font-size:9.5px;font-weight:500;text-transform:uppercase;letter-spacing:.2px}
.btn-solid{background:var(--red);color:var(--white)}
.btn-ghost{border:2px solid var(--white);color:var(--white)}
.btn-outline-red{border:1.5px solid var(--red);color:var(--navy)}

/* headings */
.section-title{color:var(--navy);font-weight:700;text-transform:uppercase;letter-spacing:-.3px}
.body-copy{color:var(--ink);font-weight:300}

/* feature cards */
.feature{position:absolute;width:200px;height:265px}
.feature h3{position:absolute;left:23px;top:108px;font-size:12.5px;font-weight:700;color:var(--white);text-transform:uppercase;white-space:nowrap}
.feature p{position:absolute;left:23px;top:132px;width:165px;font-size:10.5px;line-height:15.5px;color:#d9deea;font-weight:300}
.feature .star-icon{position:absolute;left:16px;top:22px}

/* tier cards */
.tier{position:absolute;width:201px;height:328px}
.tier .tier-art{position:absolute;left:24px;top:28px;width:44px;height:40px;border-radius:3px;background:linear-gradient(135deg,var(--navy) 0 55%,var(--red) 55% 100%)}
.tier h3{position:absolute;left:24px;top:86px;font-size:12.5px;font-weight:600;color:var(--navy);text-transform:uppercase;white-space:nowrap}
.tier .price{position:absolute;left:23px;top:102px;font-size:23px;font-weight:700;color:var(--red)}
.tier p{position:absolute;left:24px;top:140px;width:165px;font-size:10.3px;line-height:15.7px;color:#444c5e;font-weight:300}
.tier .btn{left:24px;top:242px;width:156px;height:34px}

/* form */
.field{position:absolute;border:1px solid #b9bfcc;background:var(--white);font-size:10.5px;color:#555d6f;padding:16px 0 0 19px;font-weight:400}
.field .req{color:var(--red)}

/* footer */
.footer-tag{left:0;width:1200px;text-align:center;color:var(--white);font-size:10.5px;line-height:18px;font-weight:400}
.footer-links{left:219px;top:2908px;display:flex;gap:27px;font-size:11px;color:var(--white)}
.footer-mail{right:215px;top:2908px;font-size:11px;font-weight:600;color:var(--white);display:flex;align-items:center;gap:7px}
.copyright{left:0;width:1200px;top:2958px;text-align:center;font-size:10.5px;color:var(--white)}
.to-top{left:1041px;top:2930px;width:32px;height:21px;background:var(--navy-deep);display:flex;align-items:center;justify-content:center}
</style>
</head>
<body>
<div class="page">

  <!-- HERO -->
  <svg class="layer" width="1200" height="810" viewBox="0 0 1200 810" aria-hidden="true">
    <defs>
      <linearGradient id="heroTone" x1="0" y1="0" x2="0" y2="1">
        <stop offset="0" stop-color="#3d4a72"/>
        <stop offset=".25" stop-color="#4a5576"/>
        <stop offset=".45" stop-color="#2f3e52"/>
        <stop offset="1" stop-color="#2a3648"/>
      </linearGradient>
    </defs>
    <polygon points="0,0 1200,0 1200,621 600,801 0,621" fill="url(#heroTone)"/>
    <polygon points="385,700 813,700 600,766" fill="var(--red)"/>
    <rect x="593" y="724" width="13" height="20" rx="6.5" fill="none" stroke="#fff" stroke-width="1.5"/>
    <line x1="599.5" y1="729" x2="599.5" y2="734" stroke="#fff" stroke-width="1.5"/>
  </svg>
  <div class="abs" role="img" aria-label="Aerial dusk view of suburban homes and trees with a city skyline on the horizon" style="left:0;top:0;width:1200px;height:620px"></div>

  <div class="brand" style="left:153px;top:58px;font-size:17px">
    <span class="brand-square"></span>
    <span>Tallgrove Vale<br>Management</span>
  </div>

  <nav class="nav">
    <a class="is-active">Home</a>
    <a>Services</a>
    <a>About</a>
    <a>Contact</a>
  </nav>

  <svg class="abs" style="left:568px;top:223px" width="64" height="61" viewBox="0 0 100 95" aria-hidden="true">
    <polygon points="50,0 61,35 98,35 68,57 79,91 50,70 21,91 32,57 2,35 39,35" fill="#fff"/>
  </svg>
  <div class="abs hero-kicker">CLEVELAND - AKRON · PROPERTY MANAGEMENT</div>
  <h1 class="abs hero-title">A True Partner,<br>Not Just A Vendor.</h1>
  <div class="btn btn-solid" style="left:466px;top:445px;width:131px;height:33px">Explore Services</div>
  <div class="btn btn-ghost" style="left:603px;top:445px;width:132px;height:33px">Get A Proposal</div>

  <!-- ABOUT -->
  <h2 class="abs section-title" style="left:186px;top:896px;font-size:34px;line-height:38px">Expertise Rooted<br>In Asset Preservation</h2>
  <p class="abs body-copy" style="left:185px;top:982px;width:420px;font-size:14.5px;line-height:21.5px">The organization applies rigorously tested frameworks and data-driven methodologies to safeguard property value while elevating tenant experience.</p>
  <div class="btn btn-outline-red" style="left:185px;top:1065px;width:142px;height:34px">Learn More About Us</div>

  <svg class="abs" style="left:632px;top:797px" width="391" height="372" viewBox="0 0 100 95" preserveAspectRatio="none" role="img" aria-label="Lakeside city view at sunset with historic towers above the water, framed in a star">
    <defs>
      <linearGradient id="lakeTone" x1="0" y1="0" x2="0" y2="1">
        <stop offset="0" stop-color="#f0d2c6"/>
        <stop offset=".38" stop-color="#c98a6a"/>
        <stop offset=".5" stop-color="#6b4a3a"/>
        <stop offset=".75" stop-color="#8a7f8c"/>
        <stop offset="1" stop-color="#6f7fa6"/>
      </linearGradient>
    </defs>
    <polygon points="50,0 61,35 98,35 68,57 79,91 50,70 21,91 32,57 2,35 39,35" fill="url(#lakeTone)"/>
  </svg>

  <!-- FEATURES -->
  <div class="feature" style="left:186px;top:1225px">
    <svg class="layer" width="200" height="265" viewBox="0 0 200 265" aria-hidden="true">
      <polygon points="0,0 200,0 200,234 100,265 0,234" fill="var(--navy)"/>
      <polygon points="42,240 158,240 100,258" fill="var(--red)"/>
    </svg>
    <svg class="star-icon" width="78" height="74" viewBox="0 0 100 95" aria-hidden="true">
      <polygon points="50,0 61,35 98,35 68,57 79,91 50,70 21,91 32,57 2,35 39,35" fill="#fff"/>
      <path d="M50 38 l8 3 v7 c0 5-4 8-8 10 c-4-2-8-5-8-10 v-7z" fill="none" stroke="var(--navy)" stroke-width="1.8"/>
      <path d="M46 48 l3 3 l5-6" fill="none" stroke="var(--navy)" stroke-width="1.8"/>
    </svg>
    <h3>Asset Preservation</h3>
    <p>Rigorously tested frameworks safeguard property value through proactive maintenance and strategic oversight.</p>
  </div>

  <div class="feature" style="left:395px;top:1225px">
    <svg class="layer" width="200" height="265" viewBox="0 0 200 265" aria-hidden="true">
      <polygon points="0,0 200,0 200,234 100,265 0,234" fill="var(--navy)"/>
      <polygon points="42,240 158,240 100,258" fill="var(--red)"/>
    </svg>
    <svg class="star-icon" width="78" height="74" viewBox="0 0 100 95" aria-hidden="true">
      <polygon points="50,0 61,35 98,35 68,57 79,91 50,70 21,91 32,57 2,35 39,35" fill="var(--red)"/>
      <path d="M41 52 l6-6 l4 4 l8-8 M54 42 h5 v5" fill="none" stroke="#fff" stroke-width="1.8"/>
    </svg>
    <h3>Data-Driven Growth</h3>
    <p>Advanced analytics and performance metrics drive decisions that maximize occupancy and rental yields.</p>
  </div>

  <div class="feature" style="left:603px;top:1225px">
    <svg class="layer" width="200" height="265" viewBox="0 0 200 265" aria-hidden="true">
      <polygon points="0,0 200,0 200,234 100,265 0,234" fill="var(--navy)"/>
      <polygon points="42,240 158,240 100,258" fill="var(--red)"/>
    </svg>
    <svg class="star-icon" width="78" height="74" viewBox="0 0 100 95" aria-hidden="true">
      <polygon points="50,0 61,35 98,35 68,57 79,91 50,70 21,91 32,57 2,35 39,35" fill="#fff"/>
      <circle cx="50" cy="41" r="3" fill="none" stroke="var(--navy)" stroke-width="1.6"/>
      <circle cx="42" cy="45" r="2.4" fill="none" stroke="var(--navy)" stroke-width="1.6"/>
      <circle cx="58" cy="45" r="2.4" fill="none" stroke="var(--navy)" stroke-width="1.6"/>
      <path d="M44 56 c0-6 12-6 12 0" fill="none" stroke="var(--navy)" stroke-width="1.6"/>
    </svg>
    <h3>Tenant Satisfaction</h3>
    <p>Elevated tenant experiences through responsive communication, transparent processes, and quality service.</p>
  </div>

  <div class="feature" style="left:809px;top:1225px">
    <svg class="layer" width="200" height="265" viewBox="0 0 200 265" aria-hidden="true">
      <polygon points="0,0 200,0 200,234 100,265 0,234" fill="var(--navy)"/>
      <polygon points="42,240 158,240 100,258" fill="var(--red)"/>
    </svg>
    <svg class="star-icon" width="78" height="74" viewBox="0 0 100 95" aria-hidden="true">
      <polygon points="50,0 61,35 98,35 68,57 79,91 50,70 21,91 32,57 2,35 39,35" fill="#fff"/>
      <circle cx="50" cy="46" r="8" fill="none" stroke="var(--navy)" stroke-width="1.6"/>
      <circle cx="50" cy="46" r="3.5" fill="none" stroke="var(--navy)" stroke-width="1.6"/>
    </svg>
    <h3>Proactive Maintenance</h3>
    <p style="top:138px">Scheduled inspections and preventive care reduce costly repairs while extending asset lifecycles.</p>
  </div>

  <!-- SERVICE TIERS -->
  <svg class="abs" style="left:0;top:1515px" width="1200" height="630" viewBox="0 0 1200 630" aria-hidden="true">
    <polygon points="0,180 600,0 1200,180 1200,627 0,627" fill="var(--mist)"/>
  </svg>
  <h2 class="abs section-title" style="left:0;width:1200px;top:1632px;text-align:center;font-size:33px">Our Service Tiers</h2>
  <p class="abs body-copy" style="left:0;width:1200px;top:1673px;text-align:center;font-size:14.5px;font-weight:400;color:#4a5266">Tailored solutions for properties of all sizes</p>

  <div class="tier" style="left:185px;top:1719px">
    <svg class="layer" width="201" height="328" viewBox="0 0 201 328" aria-hidden="true"><polygon points="1,1 200,1 200,296 100.5,327 1,296" fill="#fff" stroke="var(--navy)" stroke-width="1.5"/></svg>
    <div class="tier-art" role="img" aria-label="House with keys icon"></div>
    <h3>Basic Service</h3><div class="price">$99.00</div>
    <p>Describe important details like price, value, length of service, and why it's unique. Or use these sections to showcase different key values of your products or services.</p>
    <div class="btn btn-solid">View Details</div>
  </div>
  <div class="tier" style="left:394px;top:1719px">
    <svg class="layer" width="201" height="328" viewBox="0 0 201 328" aria-hidden="true"><polygon points="1,1 200,1 200,296 100.5,327 1,296" fill="#fff" stroke="var(--navy)" stroke-width="1.5"/></svg>
    <div class="tier-art" role="img" aria-label="Apartment building icon"></div>
    <h3>Intermediate Service</h3><div class="price">$149.00</div>
    <p>Describe important details like price, value, length of service, and why it's unique. Or use these sections to showcase different key values of your products or services.</p>
    <div class="btn btn-solid">View Details</div>
  </div>
  <div class="tier" style="left:602px;top:1719px">
    <svg class="layer" width="201" height="328" viewBox="0 0 201 328" aria-hidden="true"><polygon points="1,1 200,1 200,296 100.5,327 1,296" fill="#fff" stroke="var(--navy)" stroke-width="1.5"/></svg>
    <div class="tier-art" role="img" aria-label="Office towers icon"></div>
    <h3>Advanced Service</h3><div class="price">$199.00</div>
    <p>Describe important details like price, value, length of service, and why it's unique. Or use these sections to showcase different key values of your products or services.</p>
    <div class="btn btn-solid">View Details</div>
  </div>
  <div class="tier" style="left:809px;top:1719px">
    <svg class="layer" width="201" height="328" viewBox="0 0 201 328" aria-hidden="true"><polygon points="1,1 200,1 200,296 100.5,327 1,296" fill="#fff" stroke="var(--navy)" stroke-width="1.5"/></svg>
    <div class="tier-art" role="img" aria-label="Handshake with growth chart icon"></div>
    <h3>Advanced+ Service</h3><div class="price">$249.00</div>
    <p>Describe important details like price, value, length of service, and why it's unique. Or use these sections to showcase different key values of your products or services.</p>
    <div class="btn btn-solid">View Details</div>
  </div>

  <!-- PROPOSAL -->
  <div class="abs" role="img" aria-label="Aerial view of a downtown skyline beside a river and bridge at sunset" style="left:180px;top:2226px;width:378px;height:418px;clip-path:polygon(0 0,100% 0,100% 87%,50% 100%,0 87%);background:linear-gradient(180deg,#b9a8c8 0%,#d6a7a0 22%,#a66a5e 45%,#5a5a78 70%,#5f8aa0 100%)"></div>

  <h2 class="abs section-title" style="left:601px;top:2243px;font-size:32px;line-height:35px">Request A Tailored<br>Proposal</h2>
  <p class="abs body-copy" style="left:600px;top:2320px;width:400px;font-size:13.5px;line-height:20.5px;font-weight:400">Submit the form to initiate a consultative assessment and explore solutions aligned with your objectives.</p>
  <div class="field" style="left:600px;top:2380px;width:207px;height:37px">First Name <span class="req">*</span></div>
  <div class="field" style="left:812px;top:2380px;width:207px;height:37px">Last Name <span class="req">*</span></div>
  <div class="field" style="left:600px;top:2423px;width:419px;height:38px">Email <span class="req">*</span></div>
  <div class="field" style="left:600px;top:2469px;width:420px;height:111px">Message</div>
  <div class="btn btn-solid" style="left:600px;top:2588px;width:107px;height:31px;font-size:9px">Send Message</div>

  <!-- FOOTER -->
  <svg class="abs" style="left:0;top:2690px" width="1200" height="301" viewBox="0 0 1200 301" aria-hidden="true">
    <polygon points="0,209 600,10 1200,209 1200,301 0,301" fill="var(--navy)"/>
  </svg>
  <div class="brand" style="left:530px;top:2745px;font-size:16px">
    <span class="brand-square"></span>
    <span>Tallgrove Vale<br>Management</span>
  </div>
  <div class="abs footer-tag" style="top:2816px">Professional property management solutions for Cleveland-Akron area.<br>A true partner, not just a vendor.</div>
  <div class="abs" style="left:212px;top:2890px;width:780px;height:1px;background:rgba(255,255,255,.18)"></div>
  <div class="abs footer-links"><span>Home</span><span>Services</span><span>About</span><span>Contact</span></div>
  <div class="abs footer-mail">
    <svg width="10" height="8" viewBox="0 0 10 8" aria-hidden="true"><rect width="10" height="8" fill="var(--red)"/><path d="M0 0 l5 4 l5-4" fill="none" stroke="var(--navy)" stroke-width="1"/></svg>
    info@tallgrovevalemanagement.com
  </div>
  <div class="abs to-top"><svg width="8" height="5" viewBox="0 0 8 5" aria-hidden="true"><path d="M1 4 l3-3 l3 3" fill="none" stroke="#fff" stroke-width="1.2"/></svg></div>
  <div class="abs copyright">© 2026 Tallgrove Vale Management LLC. All rights reserved.</div>

</div>
</body>
</html>
```